Plivora Display Ads For Women (300x250 pixel)

We need ads for plivora display. Please use the attached image to create GIF file ads. The ads needs to have the Bidmarlow logo (attatched) and the slogan "Up To 80% Off Retail". The ads should have different background variation but the product or item should be center of attention.

Dimension: 300 by 250 pixel
File Type: GIF

Target Market(s)

Women

Industry/Entity Type

Plivora

Font styles to use
Sans Serif

Requirements
Must have
• "View Now" button

```html
<!DOCTYPE html>
<html lang="en">
<head>
<meta charset="utf-8">
<title>Bidmarlow Display Ads</title>
<link href="https://fonts.googleapis.com/css2?family=Josefin+Sans:wght@300&family=Oswald:wght@400;500;600&display=swap" rel="stylesheet">
<style>
  :root {
    --canvas-bg: #d4ccf6;
    --sample-bg: #ece7fc;
    --sample-text: #8a78b0;
    --ad-center: #fffef2;
    --ad-edge: #fde98c;
    --ink: #111111;
    --sale-red: #c4161c;
    --button-bg: #0b0b0b;
    --button-text: #ffffff;
  }
  * { margin: 0; padding: 0; box-sizing: border-box; }
  html, body { width: 1200px; height: 693px; overflow: hidden; }
  body { background: var(--canvas-bg); position: relative; font-family: "Oswald", sans-serif; }

  .ad {
    position: absolute;
    width: 367px;
    height: 306px;
    overflow: hidden;
    background: radial-gradient(ellipse at 55% 50%, var(--ad-center) 0%, #fff7c8 45%, var(--ad-edge) 100%);
  }
  .ad--1 { left: 32px;  top: 32px; }
  .ad--2 { left: 416px; top: 32px; }
  .ad--3 { left: 801px; top: 32px; }
  .ad--4 { left: 32px;  top: 355px; }
  .ad--5 { left: 416px; top: 355px; }

  .brand {
    position: absolute;
    top: 14px;
    left: 0;
    width: 100%;
    text-align: center;
    font-family: "Josefin Sans", sans-serif;
    font-weight: 300;
    font-size: 33px;
    letter-spacing: 1px;
    color: var(--ink);
  }

  .product {
    position: absolute;
    left: 82px;
    top: 62px;
    width: 220px;
    height: 232px;
    border-radius: 46%;
  }
  .product--gold   { background: radial-gradient(circle at 50% 40%, #ffffff 0%, #e8e6ea 40%, #d6ae52 75%, rgba(214,174,82,0) 100%); }
  .product--rose   { background: radial-gradient(circle at 45% 40%, #f27fb6 0%, #5b5b62 40%, #1c1c1f 70%, rgba(28,28,31,0) 100%); }
  .product--pink   { background: radial-gradient(circle at 50% 35%, #f59ad0 0%, #d24fa0 30%, #1a1a1d 65%, rgba(26,26,29,0) 100%); }
  .product--trio   { background: radial-gradient(circle at 50% 35%, #e0338a 0%, #6fb7e8 30%, #c9c9cf 60%, rgba(201,201,207,0) 100%); }
  .product--silver { background: radial-gradient(circle at 50% 40%, #ffffff 0%, #dcdde3 45%, #d9b25e 72%, rgba(217,178,94,0) 100%); }

  .offer {
    position: absolute;
    left: 20px;
    top: 214px;
    color: var(--ink);
    line-height: 1;
  }
  .offer__lead { font-size: 11px; font-weight: 500; display: block; }
  .offer__amount { color: var(--sale-red); font-size: 38px; font-weight: 500; display: block; margin-top: -1px; }
  .offer__amount small { font-size: 22px; }
  .offer__off { font-size: 40px; font-weight: 600; display: block; margin-top: -6px; }
  .offer__off small { font-size: 15px; font-weight: 500; margin-left: 2px; }

  .cta {
    position: absolute;
    left: 239px;
    top: 263px;
    width: 119px;
    height: 27px;
    background: var(--button-bg);
    border-radius: 3px;
    color: var(--button-text);
    font-size: 15px;
    letter-spacing: 2px;
    display: flex;
    align-items: center;
    justify-content: center;
    gap: 4px;
    text-decoration: none;
  }
  .cta svg { width: 7px; height: 9px; }

  .samples {
    position: absolute;
    left: 801px;
    top: 355px;
    width: 367px;
    height: 306px;
    background: var(--sample-bg);
    display: flex;
    align-items: center;
    justify-content: center;
    font-family: "Josefin Sans", sans-serif;
    font-weight: 300;
    font-size: 36px;
    letter-spacing: 1px;
    color: var(--sample-text);
  }
</style>
</head>
<body>

<section class="ad ad--1">
  <div class="brand">BIDMARLOW</div>
  <div class="product product--gold" role="img" aria-label="Gold ring with pavé diamonds and a large solitaire"></div>
  <div class="offer"><span class="offer__lead">UP TO</span><span class="offer__amount">80<small>%</small></span><span class="offer__off">OFF<small>RETAIL</small></span></div>
  <a class="cta" href="#">VIEW NOW<svg viewBox="0 0 7 9"><path d="M0 0 L7 4.5 L0 9Z" fill="#fff"/></svg></a>
</section>

<section class="ad ad--2">
  <div class="brand">BIDMARLOW</div>
  <div class="product product--rose" role="img" aria-label="Black flower ring set with pink centre stone"></div>
  <div class="offer"><span class="offer__lead">UP TO</span><span class="offer__amount">80<small>%</small></span><span class="offer__off">OFF<small>RETAIL</small></span></div>
  <a class="cta" href="#">VIEW NOW<svg viewBox="0 0 7 9"><path d="M0 0 L7 4.5 L0 9Z" fill="#fff"/></svg></a>
</section>

<section class="ad ad--3">
  <div class="brand">BIDMARLOW</div>
  <div class="product product--pink" role="img" aria-label="Black ring set with pink stones"></div>
  <div class="offer"><span class="offer__lead">UP TO</span><span class="offer__amount">80<small>%</small></span><span class="offer__off">OFF<small>RETAIL</small></span></div>
  <a class="cta" href="#">VIEW NOW<svg viewBox="0 0 7 9"><path d="M0 0 L7 4.5 L0 9Z" fill="#fff"/></svg></a>
</section>

<section class="ad ad--4">
  <div class="brand">BIDMARLOW</div>
  <div class="product product--trio" role="img" aria-label="Silver ring with pink and blue stones"></div>
  <div class="offer"><span class="offer__lead">UP TO</span><span class="offer__amount">80<small>%</small></span><span class="offer__off">OFF<small>RETAIL</small></span></div>
  <a class="cta" href="#">VIEW NOW<svg viewBox="0 0 7 9"><path d="M0 0 L7 4.5 L0 9Z" fill="#fff"/></svg></a>
</section>

<section class="ad ad--5">
  <div class="brand">BIDMARLOW</div>
  <div class="product product--silver" role="img" aria-label="Silver and gold filigree ring with marquise stone"></div>
  <div class="offer"><span class="offer__lead">UP TO</span><span class="offer__amount">80<small>%</small></span><span class="offer__off">OFF<small>RETAIL</small></span></div>
  <a class="cta" href="#">VIEW NOW<svg viewBox="0 0 7 9"><path d="M0 0 L7 4.5 L0 9Z" fill="#fff"/></svg></a>
</section>

<div class="samples">SAMPLES</div>

</body>
</html>
```